Harbourline Panels Brochure

Harbourline Panels New Brochure Brief
Harbourline Panels are manufacturers of kitchen and wardrobe doors. We have 2 target markets, one is business to business and the other business to residential customers.
The main message of our business to residential is to inform them that they can give their kitchen or wardrobe a facelift by just replacing doors and save thousands of dollars by doing this partial renovation. However, this is in direct conflict with our business to business customers (kitchen and wardrobe companies) who buy doors from us and sell complete new kitchens and built in wardrobes to the same residential customers.
Please find links to the Harbourline Panels brochure and website below for your reference. The current dimensions of the brochure is approx. 21cmH x 29.7cmW. https://harbourlinepanels.com.au/harbourlinepanelsbrochure-2/ https://harbourlinepanels.com.au/
I would like to keep the layout of the brochure internal pages consistent with the current design, however, I am open to your ideas. The orange colour as seen on the front page should be a dominant theme as it’s based on our logo however not too overpowering, I prefer to cover to be white. I would like a new front page design, changing the door photos (they will be shades of white, not coloured) and also delete the words ‘ultimate door collection’. Heading to be along the lines of “Custom made kitchen and wardrobe doors”.
On the internal pages, some new door designs will be added and some deleted. s. We are thinking of changing all the door colours to shades of white but also stating that Harbourline Panels can colour match to any major Australian paint brand.
I would like to include a page for Wardrobe Doors with some photos, text and layout options (photo attached). Please add in the before and after images. Please create a before and after using Rob's kitchen in same layout as wardrobe before and after. Please ensure oven is cut from after image. Please add in the photos attached in this brief.
We would also like to include a FAQs section. Some more text describing our product, such as raw material, thickness of doors, painted or unpainted finish and delivery information is to be added.
Re: the ‘edges’ top of page 3; some will be deleted and one new type of edge will be added.
From page 4 onwards, there are different shapes at the bottom of each door design. We are looking for a new way to communicate this as at the moment it is taking up too much room and people do not readily understand that these door patterns can be supplied in the shapes shown in the little diagrams below them.
Please keep in mind all this information will be given at the time of design. I would like to possibly keep the brochure at 8 pages (as it is now). There may be some other changes along the way as this is still in the preliminary stage. Please include the image of our showroom in the brochure mock up.
I look forward to your reply.
Kind Regards,
Greta
* Please note, the images attach with the individual doors need to be changed to some neutral shades such as white, off white, grey, cream etc (similar to the website: https://harbourlinepanels.com.au/kitchen-doors/)

```html
<!DOCTYPE html>
<html lang="en">
<head>
<meta charset="utf-8">
<title>Harbourline Panels Brochure</title>
<link href="https://fonts.googleapis.com/css2?family=Montserrat:ital,wght@0,400;0,500;0,600;0,700;0,800;1,400&display=swap" rel="stylesheet">
<style>
:root{
  --orange:#f08a1e;
  --ink:#222222;
  --grey:#555555;
  --line:#cfcfcf;
  --paper:#ffffff;
  --bg:#ffffff;
  --cream:#efe4db;
}
*{box-sizing:border-box;margin:0;padding:0}
html,body{width:1200px;height:1200px;overflow:hidden;background:var(--bg);font-family:'Montserrat',sans-serif;color:var(--ink)}
.spread{position:absolute;left:56px;width:1093px;height:387px;background:var(--paper);overflow:hidden}
.cover-spread{top:179px}
.inner-spread{top:626px}
.abs{position:absolute}

/* cover */
.back-photo{left:0;top:0;width:546px;height:387px;background:linear-gradient(180deg,#f3ebe4 0%,#efe4db 60%,#e9ddd2 100%)}
.front-photo{left:546px;top:0;width:547px;height:387px;background:linear-gradient(180deg,#f6f6f5 0%,#ececea 45%,#c9c9c6 75%,#a9a9a6 100%)}
.front-photo-right{left:931px;top:0;width:162px;height:387px;background:linear-gradient(180deg,#ececec 0%,#b9bcbf 45%,#7e8082 75%,#6c6d6e 100%)}
.brand{display:flex;align-items:center;gap:5px;font-weight:700;color:var(--ink);line-height:1.05}
.brand-mark{width:10px;height:10px;background:var(--orange);flex:none}
.cover-brand{left:592px;top:60px;font-size:15px;width:120px}
.back-brand{left:22px;top:310px;font-size:11px;width:80px}
.back-divider{left:107px;top:281px;width:1px;height:87px;background:#444}
.contact-title{left:135px;top:285px;font-size:17px;font-weight:700;color:var(--orange);letter-spacing:.5px}
.contact{font-size:8.6px;font-weight:600;color:var(--ink);line-height:11px;display:flex;gap:6px}
.contact svg{flex:none;margin-top:1px}
.title-light{left:590px;top:182px;font-size:34px;font-weight:400;letter-spacing:1px;color:#1c1c1c}
.title-orange{left:590px;top:214px;font-size:53px;font-weight:800;color:var(--orange);letter-spacing:3px}
.title-amp{left:871px;top:214px;font-size:52px;font-weight:400;color:#1c1c1c}
.title-band{left:593px;top:275px;width:353px;height:40px;background:var(--orange);color:#fff;font-size:28px;font-weight:800;letter-spacing:1px;display:flex;align-items:center;padding-left:10px}
.cover-url{left:593px;top:334px;font-size:12.5px;font-weight:400;color:#1c1c1c;white-space:nowrap}
.cover-url b{font-weight:700}
.cover-rule{left:797px;top:346px;width:296px;height:1px;background:#e8e8e8}

/* inner left page */
.h-light{left:28px;top:20px;font-size:20px;font-weight:400;letter-spacing:.5px}
.h-bold{left:28px;top:45px;font-size:21px;font-weight:800;color:var(--orange);letter-spacing:.5px}
.h-rule{left:28px;top:71px;width:222px;height:1px;background:var(--line)}
.badge{left:268px;top:37px}
.intro{left:28px;top:79px;width:235px;font-size:5.2px;line-height:6.6px;color:var(--grey)}
.feature{width:150px}
.feature .icon{position:absolute;left:0;top:0;width:14px;height:14px;border:1.2px solid var(--orange);border-radius:50%}
.feature .icon::after{content:"";position:absolute;left:3.5px;top:3.5px;width:5px;height:5px;border-radius:50%;background:#777}
.feature h3{margin-left:21px;font-size:7.2px;font-weight:700;color:var(--orange);line-height:9px}
.feature p{margin-left:21px;font-size:5px;line-height:6.6px;color:var(--grey)}
.dashed{width:0;border-left:1px dashed #aaa}
.order-title{left:28px;top:256px;font-size:11.5px;font-weight:700;color:var(--orange);letter-spacing:.4px}
.order-rule{left:28px;top:272px;width:166px;height:1px;background:var(--line)}
.step{display:flex;gap:9px;align-items:flex-start;width:170px}
.step .num{flex:none;width:26px;height:26px;border-radius:50%;border:2px solid var(--orange);font-size:5.5px;font-weight:600;color:#444;display:flex;align-items:center;justify-content:center;text-align:center;line-height:6px}
.step p{font-size:7.6px;line-height:9.4px;color:var(--grey);padding-top:2px}
.steps-divider{left:215px;top:285px;width:1px;height:62px;background:var(--line)}
.deliver{left:382px;top:302px;font-size:8.4px;line-height:8px;text-align:right;color:#333}
.deliver b{color:var(--orange);font-weight:700}
.truck{left:438px;top:300px;width:57px;height:44px;background:linear-gradient(180deg,#3a4a8a 0%,#222 100%);border-radius:2px}
.photo{position:absolute;height:98px;width:76px}
.tag{position:absolute;bottom:3px;font-size:5px;color:#fff;padding:1px 5px}
.tag-before{left:0;background:rgba(90,90,90,.7)}
.tag-after{right:0;background:var(--orange)}
.cap{font-size:7.4px;font-weight:700;color:var(--orange);line-height:8px}
.cap span{display:block;font-size:5px;font-weight:400;color:#333;line-height:7px}
.folio-rule{left:40px;top:369px;width:1013px;height:1px;background:#bbb}
.folio{top:364px;font-size:6px;color:#666;background:#eee;padding:1px 2px}

/* right page */
.range{left:588px;font-size:18px;font-weight:400;color:#1c1c1c;white-space:nowrap}
.range b{color:var(--orange);font-weight:800}
.range i{font-size:5.8px;color:#333;margin-left:4px}
.door{position:absolute;box-shadow:0 1px 2px rgba(0,0,0,.15)}
.code{position:absolute;font-size:8.5px;color:#222;text-align:center;border-top:1px dashed #888;border-bottom:1px dashed #888;line-height:10px;padding:0 2px;white-space:nowrap}
.range-rule{left:588px;top:206px;width:478px;height:1px;background:#aaa}
</style>
</head>
<body>

<section class="spread cover-spread">
  <div class="abs back-photo" role="img" aria-label="Faded view of the showroom wall lined with white sample doors"></div>
  <div class="abs front-photo" role="img" aria-label="Showroom with curved walls of white kitchen and wardrobe sample doors"></div>
  <div class="abs front-photo-right" role="img" aria-label="Showroom corner with grey carpet and framed door samples"></div>

  <div class="abs brand back-brand"><span class="brand-mark"></span><span>Harbourline Panels</span></div>
  <div class="abs back-divider"></div>
  <div class="abs contact-title">CONTACT US</div>
  <div class="abs contact" style="left:135px;top:312px">
    <svg width="6" height="8" viewBox="0 0 6 8"><path d="M3 0a3 3 0 0 0-3 3c0 2 3 5 3 5s3-3 3-5a3 3 0 0 0-3-3z" fill="#f08a1e"/></svg>
    <span>14 Marlow Road<br>Kellmont NSW 2170</span></div>
  <div class="abs contact" style="left:135px;top:343px">
    <svg width="7" height="7" viewBox="0 0 8 8"><path d="M1 0l2 2-1 1.5c.6 1.2 1.3 1.9 2.5 2.5L6 5l2 2-1 1C3 8 0 5 0 1z" fill="#f08a1e"/></svg>
    <span>(02) 9000 4444</span></div>
  <div class="abs contact" style="left:312px;top:310px">
    <svg width="7" height="7" viewBox="0 0 8 8"><rect x="1" y="0" width="6" height="8" rx="1" fill="#f08a1e"/></svg>
    <span>(02) 9000 4777</span></div>
  <div class="abs contact" style="left:312px;top:326px">
    <svg width="7" height="6" viewBox="0 0 8 6"><rect width="8" height="6" fill="#f08a1e"/><path d="M0 0l4 3 4-3" stroke="#fff" fill="none" stroke-width=".8"/></svg>
    <span>sales@harbourlinepanels.com.au</span></div>
  <div class="abs contact" style="left:312px;top:342px">
    <svg width="7" height="7" viewBox="0 0 8 8"><circle cx="4" cy="4" r="3.5" fill="none" stroke="#f08a1e"/><path d="M.5 4h7M4 .5v7" stroke="#f08a1e" stroke-width=".7"/></svg>
    <span>www.harbourlinepanels.com.au</span></div>

  <div class="abs brand cover-brand"><span class="brand-mark"></span><span>Harbourline Panels</span></div>
  <div class="abs title-light">CUSTOM MADE</div>
  <div class="abs title-orange">KITCHEN</div>
  <div class="abs title-amp">&amp;</div>
  <div class="abs title-band">WARDROBE DOORS</div>
  <div class="abs cover-url">www.<b>harbourlinepanels</b>.com.au</div>
  <div class="abs cover-rule"></div>
</section>

<section class="spread inner-spread">
  <h1 class="abs h-light">KITCHEN AND</h1>
  <h2 class="abs h-bold">WARDROBE DOORS</h2>
  <div class="abs h-rule"></div>
  <svg class="abs badge" width="60" height="60" viewBox="0 0 60 60"><circle cx="30" cy="30" r="29" fill="#1f3f8f"/><circle cx="30" cy="30" r="21" fill="#fff"/><circle cx="30" cy="30" r="15" fill="#f08a1e"/></svg>
  <p class="abs intro">Kitchen renovations and bedroom makeovers are quick and cost-efficient when you simply replace the doors and panels. It can save you thousands of dollars and increase the value of your home.</p>

  <div class="abs dashed" style="left:35px;top:134px;height:78px"></div>
  <div class="abs dashed" style="left:205px;top:134px;height:76px"></div>

  <div class="abs feature" style="left:28px;top:113px"><span class="icon"></span><h3>Save time and money</h3><p>Competitive prices and fast delivery of custom made kitchen and wardrobe doors Australia wide. Polyurethane painted doors ready in approx. 15 working days.</p></div>
  <div class="abs feature" style="left:28px;top:159px"><span class="icon"></span><h3>Huge range of designs</h3><p>Choose from plain, shaker style or intricately patterned heritage design, even custom designs and angled doors.</p></div>
  <div class="abs feature" style="left:28px;top:201px"><span class="icon"></span><h3>Quality Australian made material</h3><p>Doors are made from 18mm white satin moisture resistant (MR) MDF or optionally in 16, 21 or 25mm thickness. All guaranteed to conform to Australian Quality Standards.</p></div>
  <div class="abs feature" style="left:197px;top:113px"><span class="icon"></span><h3>Hardware and decorative</h3><p>We supply Norvik soft closing hinges, door handles and wardrobe track kits. Flutes, corbels, rosettes, fretwork and capping.</p></div>
  <div class="abs feature" style="left:197px;top:158px"><span class="icon"></span><h3>Polyurethane painting</h3><p>Doors can be supplied painted in polyurethane, with a matt, satin, semi gloss or high gloss finish in the colour of your choice.</p></div>
  <div class="abs feature" style="left:197px;top:204px"><span class="icon"></span><h3>Trade customers:</h3><p>Cut to size or router only service with pick up and delivery to your premises or painter. Raw doors ready in approx. 5 working days.</p></div>

  <div class="abs order-title">HOW TO PLACE AN ORDER</div>
  <div class="abs order-rule"></div>
  <div class="abs step" style="left:27px;top:282px"><span class="num">STEP<br>01</span><p>Choose your door design, paint colour and finish and accessories</p></div>
  <div class="abs step" style="left:27px;top:318px"><span class="num">STEP<br>02</span><p>DIY measure your doors, fill out our Order Form or contact an installer to measure and install</p></div>
  <div class="abs steps-divider"></div>
  <div class="abs step" style="left:229px;top:282px;width:150px"><span class="num">STEP<br>03</span><p>Check and pay our quote to go ahead with the order</p></div>
  <div class="abs step" style="left:229px;top:318px;width:150px"><span class="num">STEP<br>04</span><p>Your doors will be ready for delivery in approx 15 working days</p></div>
  <div class="abs deliver">WE<br>DELIVER<br><b>AUSTRALIA<br>WIDE</b></div>
  <div class="abs truck" role="img" aria-label="Delivery truck illustration with Australian flag"></div>

  <div class="photo" style="left:347px;top:22px;background:linear-gradient(180deg,#eeeeec,#b9b5ae)" role="img" aria-label="Kitchen before new doors"><span class="tag tag-before">BEFORE</span></div>
  <div class="photo" style="left:426px;top:22px;background:linear-gradient(180deg,#f3f3f1,#6f7371)" role="img" aria-label="Kitchen after new doors"><span class="tag tag-after">AFTER</span></div>
  <div class="abs cap" style="left:347px;top:125px">New Kitchen Doors =<span>A quick and cost-effective kitchen renovation</span></div>
  <div class="photo" style="left:347px;top:146px;height:100px;background:linear-gradient(180deg,#6a4330,#a0785a)" role="img" aria-label="Bedroom wardrobe before new doors"><span class="tag tag-before">BEFORE</span></div>
  <div class="photo" style="left:426px;top:146px;height:100px;background:linear-gradient(180deg,#e8e9ea,#8d9197)" role="img" aria-label="Bedroom wardrobe after new doors"><span class="tag tag-after">AFTER</span></div>
  <div class="abs cap" style="left:347px;top:252px">New Wardrobe Doors =<span>An instant bedroom makeover</span></div>

  <div class="abs range" style="top:20px"><b>RANGE</b> 4210-4212<i>Top of the range classic bolection mould doors crafted from a single piece of material</i></div>
  <div class="door" style="left:590px;top:46px;width:73px;height:134px;background:#f1eee6" role="img" aria-label="Door 4210 HVA in off white"></div>
  <div class="door" style="left:686px;top:46px;width:73px;height:134px;background:#d9dacf" role="img" aria-label="Door 4210 HPA in pale sage"></div>
  <div class="door" style="left:782px;top:46px;width:73px;height:132px;background:#c6c7c9" role="img" aria-label="Door 4210 HKA in light grey"></div>
  <div class="door" style="left:879px;top:46px;width:73px;height:132px;background:#eaeee4" role="img" aria-label="Door 4211 HPA in pale green white"></div>
  <div class="door" style="left:973px;top:46px;width:73px;height:134px;background:#f2f5f9" role="img" aria-label="Door 4212 HPA in white"></div>
  <div class="code" style="left:600px;top:186px;width:55px">4210 HVA</div>
  <div class="code" style="left:696px;top:186px;width:55px">4210 HPA</div>
  <div class="code" style="left:786px;top:186px;width:55px">4210 HKA</div>
  <div class="code" style="left:883px;top:186px;width:55px">4211 HPA</div>
  <div class="code" style="left:980px;top:186px;width:55px">4212 HPA</div>

  <div class="abs range-rule"></div>
  <div class="abs range" style="top:205px"><b>RANGE</b> 4101-4103<i>Elegant and sophisticated design for an upmarket kitchen</i></div>
  <div class="door" style="left:589px;top:230px;width:59px;height:107px;background:#e9f0f7" role="img" aria-label="Door 4101 HIA in ice white"></div>
  <div class="door" style="left:657px;top:230px;width:59px;height:107px;background:#f3f2ee" role="img" aria-label="Door 4102 HIA in white"></div>
  <div class="door" style="left:725px;top:230px;width:59px;height:107px;background:#f0f0ee" role="img" aria-label="Door 4103 HIA in white"></div>
  <div class="door" style="left:793px;top:230px;width:59px;height:107px;background:#dcdccf" role="img" aria-label="Door 4103 HJA in stone"></div>
  <div class="door" style="left:862px;top:230px;width:59px;height:107px;background:#9a9b9c" role="img" aria-label="Door 4101 HDA in grey"></div>
  <div class="door" style="left:930px;top:230px;width:59px;height:107px;background:#e2e2de" role="img" aria-label="Door 4101 HMA in light grey"></div>
  <div class="door" style="left:1000px;top:230px;width:59px;height:107px;background:#e7e7e3" role="img" aria-label="Door 4101 HTA in off white"></div>
  <div class="code" style="left:590px;top:345px;width:56px">4101 HIA</div>
  <div class="code" style="left:659px;top:345px;width:56px">4102 HIA</div>
  <div class="code" style="left:727px;top:345px;width:56px">4103 HIA</div>
  <div class="code" style="left:793px;top:345px;width:56px">4103 HJA</div>
  <div class="code" style="left:862px;top:345px;width:56px">4101 HDA</div>
  <div class="code" style="left:930px;top:345px;width:56px">4101 HMA</div>
  <div class="code" style="left:1000px;top:345px;width:56px">4101 HTA</div>

  <div class="abs folio-rule"></div>
  <div class="abs folio" style="left:20px">02</div>
  <div class="abs folio" style="left:1062px">03</div>
</section>

</body>
</html>
```